Popular Australian based wellbeing and high performance podcast needs a design

I need a new, fresh design for my Keep Rising Daily podcast image. This podcast helps and enables its listeners to do their life even better by enhancing their wellbeing, mindset, happiness and leadership. I would love to see designs that include the colour blue. The final design should communicate optimism, hope, approachability and credibility.

Target Market(s)

Target is teenagers to adults wanting to enhance their wellbeing, mindset and happiness.

Font styles to use
Other font styles liked:
• Proba Pro

Colors
33a6d7
0592cd
ffffff

Requirements
Must have
• Must include: Keep Rising Daily podcast
Nice to have
• Could include: with Mick Talvero.

```html
<!DOCTYPE html>
<html lang="en">
<head>
<meta charset="utf-8">
<title>Keep Rising Daily Podcast – Cover</title>
<link rel="stylesheet" href="https://fonts.googleapis.com/css2?family=Cabin:wght@400&display=swap">
<style>
  :root {
    --blue-light: #33a6d7;
    --blue-deep: #0592cd;
    --white: #ffffff;
    --shadow: #000000;
    --photo-warm: #8a6a45;
    --photo-dark: #2c2620;
    --photo-shirt: #6f8fc4;
  }
  html, body {
    margin: 0;
    padding: 0;
    width: 1200px;
    height: 1200px;
    overflow: hidden;
    background: var(--white);
  }
  .cover {
    display: block;
    width: 1200px;
    height: 1200px;
  }
  .cover-text {
    font-family: "Cabin", "Helvetica Neue", Arial, sans-serif;
    font-weight: 400;
    fill: var(--white);
  }
  .show-title { font-size: 118px; }
  .podcast-letter { font-size: 74px; }
  .host-with { font-size: 44px; }
  .host-name { font-size: 66px; }
</style>
</head>
<body>
<svg class="cover" viewBox="0 0 1200 1200" xmlns="http://www.w3.org/2000/svg">
  <defs>
    <filter id="panel-shadow" x="-20%" y="-20%" width="140%" height="140%">
      <feDropShadow dx="0" dy="0" stdDeviation="9" flood-color="var(--shadow)" flood-opacity="0.85"/>
    </filter>
    <radialGradient id="portrait-tone" cx="50%" cy="40%" r="65%">
      <stop offset="0%" stop-color="var(--photo-warm)"/>
      <stop offset="60%" stop-color="var(--photo-dark)"/>
      <stop offset="100%" stop-color="var(--photo-shirt)"/>
    </radialGradient>
    <clipPath id="square-clip">
      <rect x="122" y="82" width="978" height="1028"/>
    </clipPath>
  </defs>

  <!-- cover square -->
  <g class="cover-square" clip-path="url(#square-clip)">
    <rect class="cover-base" x="122" y="82" width="978" height="1028" fill="var(--shadow)"/>

    <!-- corner panels -->
    <rect class="corner-panel" x="122" y="82" width="310" height="350" fill="var(--blue-light)" filter="url(#panel-shadow)"/>
    <rect class="corner-panel" x="752" y="82" width="348" height="350" fill="var(--blue-deep)" filter="url(#panel-shadow)"/>
    <rect class="corner-panel" x="122" y="760" width="310" height="350" fill="var(--blue-deep)" filter="url(#panel-shadow)"/>
    <rect class="corner-panel" x="752" y="760" width="348" height="350" fill="var(--blue-light)" filter="url(#panel-shadow)"/>

    <!-- cross bands -->
    <rect class="cross-band" x="444" y="82" width="296" height="1028" fill="var(--blue-light)" filter="url(#panel-shadow)"/>
    <rect class="cross-band" x="122" y="444" width="978" height="304" fill="var(--blue-light)" filter="url(#panel-shadow)"/>
    <rect class="cross-core" x="524" y="82" width="140" height="1028" fill="var(--blue-deep)" filter="url(#panel-shadow)"/>
    <rect class="cross-core" x="122" y="544" width="978" height="112" fill="var(--blue-deep)" filter="url(#panel-shadow)"/>

    <!-- rings around portrait -->
    <ellipse class="ring-outer" cx="604" cy="590" rx="390" ry="400" fill="var(--blue-light)" filter="url(#panel-shadow)"/>
    <ellipse class="ring-inner" cx="604" cy="590" rx="330" ry="340" fill="var(--blue-deep)" filter="url(#panel-shadow)"/>
    <ellipse class="ring-edge" cx="604" cy="586" rx="296" ry="306" fill="var(--blue-light)"/>
  </g>

  <!-- portrait area -->
  <ellipse class="host-portrait" cx="604" cy="584" rx="276" ry="288" fill="url(#portrait-tone)"
           role="img" aria-label="Portrait photo of the podcast host smiling, wearing a light blue shirt, in a warmly lit room"/>

  <!-- title -->
  <text class="cover-text show-title" x="611" y="254" text-anchor="middle">Keep Rising Daily</text>

  <!-- curved podcast label -->
  <g class="podcast-label cover-text">
    <text class="podcast-letter" x="130" y="844">P</text>
    <text class="podcast-letter" x="156" y="882">o</text>
    <text class="podcast-letter" x="192" y="920">d</text>
    <text class="podcast-letter" x="232" y="966">c</text>
    <text class="podcast-letter" x="272" y="1006">a</text>
    <text class="podcast-letter" x="320" y="1046">s</text>
    <text class="podcast-letter" x="358" y="1090">t</text>
  </g>

  <!-- broadcast icon -->
  <g class="broadcast-icon" fill="none" stroke="var(--white)" stroke-width="11" stroke-linecap="round">
    <circle cx="204" cy="1044" r="15" fill="var(--white)" stroke="none"/>
    <path d="M180 1020 A34 34 0 0 0 180 1068"/>
    <path d="M228 1020 A34 34 0 0 1 228 1068"/>
    <path d="M162 1002 A60 60 0 0 0 162 1086"/>
    <path d="M246 1002 A60 60 0 0 1 246 1086"/>
  </g>

  <!-- host credit -->
  <text class="cover-text host-with" x="932" y="1016" text-anchor="middle">with</text>
  <text class="cover-text host-name" x="1092" y="1090" text-anchor="end">Mick Talvero</text>
</svg>
</body>
</html>
```